Business card design

I need my logo on this card, things I need the card to have on it
licensed and insured.
owner operators Derek & Milton Halvorsen
my phone number 5418237906
Disaster Recovery, Storm Damage Restoration, Proactive Disaster Plan Management, Roof Repair/Restoration Structural Repair and Reconstruction, Emergency Boarding and Tarping Service, Perimeter Fencing, Emergency Tree Removal,

```html
<!DOCTYPE html>
<html lang="en">
<head>
<meta charset="utf-8">
<title>Halvorsen Construction – Business Card</title>
<link href="https://fonts.googleapis.com/css2?family=Questrial&family=Montserrat:wght@600;700&display=swap" rel="stylesheet">
<style>
:root{
  --bg:#e9eff3;
  --card:#ffffff;
  --blue:#1493e6;
  --gray:#5f6062;
  --ink:#3a3b3d;
  --label:#c9cdd0;
  --rule:#8b8c8e;
}
*{margin:0;padding:0;box-sizing:border-box}
html,body{width:1081px;height:1200px;overflow:hidden;background:var(--bg)}
.stage{position:relative;width:1459px;height:1619px;transform:scale(0.7409);transform-origin:0 0}
.side-label{position:absolute;font-family:"Questrial",sans-serif;font-size:42px;color:var(--label);transform:rotate(-90deg);transform-origin:left top;white-space:nowrap}
.card{position:absolute;width:1050px;height:600px;background:var(--card);box-shadow:0 30px 40px -20px rgba(0,0,0,.35)}
.card-front{left:284px;top:140px}
.card-back{left:286px;top:879px}
.bands{position:absolute;inset:0;width:1050px;height:600px}
.company-name{position:absolute;display:flex;align-items:center;gap:12px;font-family:"Questrial",sans-serif;font-weight:400;color:var(--ink);line-height:1;white-space:nowrap}
.company-name .dot{display:block;background:var(--blue)}
.front-name{left:60px;top:290px;font-size:32px}
.front-name .dot{width:18px;height:18px}
.back-name{left:742px;top:200px;font-size:21px;gap:8px}
.back-name .dot{width:12px;height:12px}
.licence{position:absolute;left:66px;top:436px;font-family:"Questrial",sans-serif}
.licence .title{font-size:33px;color:var(--blue);display:block}
.licence .owners{font-size:15.5px;color:var(--ink);display:block;margin-top:4px}
.icon{position:absolute;width:48px;height:54px;left:510px}
.contact{position:absolute;left:586px;font-family:"Montserrat",sans-serif;font-weight:700;color:var(--ink);font-size:19px;line-height:30px}
.person-name{position:absolute;left:586px;top:118px;font-family:"Montserrat",sans-serif;font-weight:700;font-size:32px;color:var(--blue)}
.designation{position:absolute;left:586px;top:161px;font-family:"Montserrat",sans-serif;font-weight:600;font-size:19px;color:var(--rule)}
.rule{position:absolute;left:586px;width:398px;height:2px;background:var(--rule)}
.services-title{position:absolute;left:62px;top:72px;font-family:"Questrial",sans-serif;font-weight:400;font-size:52px;color:var(--blue)}
.services{position:absolute;left:62px;top:134px;list-style:none;font-family:"Questrial",sans-serif;font-size:35px;color:var(--ink);line-height:50px}
.services li{position:relative;padding-left:28px}
.services li::before{content:"";position:absolute;left:2px;top:20px;width:13px;height:14px;background:var(--blue);clip-path:polygon(50% 0,100% 25%,100% 75%,50% 100%,0 75%,0 25%)}
</style>
</head>
<body>
<div class="stage">
  <span class="side-label" style="left:176px;top:550px">Front Side</span>
  <span class="side-label" style="left:176px;top:1290px">Back Side</span>

  <section class="card card-front">
    <svg class="bands" viewBox="0 0 1050 600" aria-hidden="true">
      <polygon points="0,0 100,0 0,92" fill="var(--blue)"/>
      <polygon points="100,0 505,0 494,19 116,19 0,120 0,92" fill="var(--gray)"/>
      <polygon points="512,10 1050,10 1050,32 500,32" fill="var(--blue)"/>
      <polygon points="0,568 550,568 538,590 0,590" fill="var(--blue)"/>
      <polygon points="552,582 936,582 1050,482 1050,510 950,600 545,600" fill="var(--gray)"/>
      <polygon points="950,600 1050,510 1050,600" fill="var(--blue)"/>
    </svg>

    <div class="company-name front-name"><span class="dot"></span>Halvorsen Construction LLC</div>

    <div class="licence">
      <span class="title">Licensed and Insured</span>
      <span class="owners">Owner operators Derek &amp; Milton Halvorsen</span>
    </div>

    <svg class="icon" style="top:127px" viewBox="0 0 48 54" aria-hidden="true">
      <polygon points="24,0 48,13.5 48,40.5 24,54 0,40.5 0,13.5" fill="var(--blue)"/>
      <circle cx="24" cy="21" r="6" fill="none" stroke="#fff" stroke-width="2"/>
      <path d="M13 38c2-6 6-9 11-9s9 3 11 9" fill="none" stroke="#fff" stroke-width="2"/>
    </svg>
    <div class="person-name">YOUR NAME</div>
    <div class="designation">DESIGNATION</div>
    <div class="rule" style="top:195px"></div>

    <svg class="icon" style="top:286px" viewBox="0 0 48 54" aria-hidden="true">
      <polygon points="24,0 48,13.5 48,40.5 24,54 0,40.5 0,13.5" fill="var(--blue)"/>
      <path d="M15 17c0 11 7 19 18 20l2-5-5-3-3 3c-3-2-6-5-7-8l3-3-3-5z" fill="none" stroke="#fff" stroke-width="1.8" stroke-linejoin="round"/>
    </svg>
    <div class="contact" style="top:292px">5418237906</div>
    <div class="rule" style="top:337px"></div>

    <svg class="icon" style="top:361px" viewBox="0 0 48 54" aria-hidden="true">
      <polygon points="24,0 48,13.5 48,40.5 24,54 0,40.5 0,13.5" fill="var(--blue)"/>
      <rect x="13" y="18" width="22" height="14" rx="1" fill="none" stroke="#fff" stroke-width="2"/>
      <path d="M24 32v5M19 37h10" stroke="#fff" stroke-width="2"/>
    </svg>
    <div class="contact" style="top:351px">info@ridgelinemail.com<br>www.ridgelinemail.com</div>
    <div class="rule" style="top:423px"></div>

    <svg class="icon" style="top:440px" viewBox="0 0 48 54" aria-hidden="true">
      <polygon points="24,0 48,13.5 48,40.5 24,54 0,40.5 0,13.5" fill="var(--blue)"/>
      <path d="M24 39c-6-7-9-11-9-15a9 9 0 0 1 18 0c0 4-3 8-9 15z" fill="none" stroke="#fff" stroke-width="2"/>
      <circle cx="24" cy="24" r="3" fill="none" stroke="#fff" stroke-width="2"/>
    </svg>
    <div class="contact" style="top:440px">your Address&nbsp; 2223, Absd, Street,<br>Country, Ak 9951</div>
  </section>

  <section class="card card-back">
    <svg class="bands" viewBox="0 0 1050 600" aria-hidden="true">
      <polygon points="0,10 540,10 552,32 0,32" fill="var(--blue)"/>
      <polygon points="548,0 950,0 1050,88 1050,118 936,18 556,18" fill="var(--gray)"/>
      <polygon points="950,0 1050,0 1050,88" fill="var(--blue)"/>
      <polygon points="0,480 116,582 494,582 505,600 100,600 0,508" fill="var(--gray)"/>
      <polygon points="0,508 100,600 0,600" fill="var(--blue)"/>
      <polygon points="500,568 1050,568 1050,590 512,590" fill="var(--blue)"/>
    </svg>

    <h2 class="services-title">Our Services</h2>
    <ul class="services">
      <li>Disaster Recovery</li>
      <li>Storm Damage Restoration</li>
      <li>Proactive Disaster Plan Management</li>
      <li>Roof Repair/Restoration Structural<br>Repair and Reconstruction,</li>
      <li>Emergency Boarding and Tarping Service</li>
      <li>Perimeter Fencing</li>
      <li>Emergency Tree Removal</li>
    </ul>

    <div class="company-name back-name"><span class="dot"></span>Halvorsen Construction LLC</div>
  </section>
</div>
</body>
</html>
```